business card - Helicopter Flight Services, Flight School, etc.

We need a business card design for a new helicopter service.

We offer Helicopter Flight Services, Aerial Filming & Photography, Flight School, and Helicopter Tours. In that order.

Summit BladeLine, Inc.
Harold Tebbets
SummitBladeline@Mailvane.com
555-014-2786

Based at the Corvell Airport in Van Nuys, CA. The final design should communicate integrity and safety. Pictures or logos at your discretion.

Card back side - surprise me.

```html
<!DOCTYPE html>
<html lang="en">
<head>
<meta charset="utf-8">
<title>Summit BladeLine, Inc. — Business Card</title>
<link rel="stylesheet" href="https://fonts.googleapis.com/css2?family=Bodoni+Moda:wght@600;700&family=Open+Sans:wght@300;400&display=swap">
<style>
  :root {
    --stage: #d9d3ca;
    --card-black: #050505;
    --card-black-soft: #1a1a1c;
    --back-dark: #1f1315;
    --back-dark-soft: #2b1d1f;
    --ink-white: #ffffff;
    --ink-soft: #e6e6e6;
    --rule: #9a9a9a;
    --violet: #6b67c2;
    --violet-light: #a9a6e4;
    --violet-deep: #5550a8;
  }
  * { margin: 0; padding: 0; box-sizing: border-box; }
  html, body { width: 1200px; height: 892px; overflow: hidden; }
  body {
    background: var(--stage);
    display: flex;
    flex-direction: column;
    align-items: center;
    justify-content: center;
    gap: 56px;
  }
  .card {
    position: relative;
    width: 600px;
    height: 343px;
    overflow: hidden;
    box-shadow: 0 10px 28px rgba(0,0,0,.28);
  }

  /* Front */
  .card-front {
    background: linear-gradient(160deg, var(--card-black-soft) 0%, var(--card-black) 55%);
  }
  .front-swoosh { position: absolute; inset: 0; }
  .company-name {
    position: absolute;
    top: 32px;
    right: 34px;
    font-family: "Bodoni Moda", serif;
    font-weight: 700;
    font-size: 36px;
    color: var(--ink-white);
    letter-spacing: .3px;
    white-space: nowrap;
  }
  .title-rule {
    position: absolute;
    top: 92px;
    left: 150px;
    right: 30px;
    height: 1px;
    background: var(--rule);
  }
  .person-name {
    position: absolute;
    top: 122px;
    left: 126px;
    font-family: "Open Sans", sans-serif;
    font-weight: 300;
    font-size: 18px;
    color: var(--ink-soft);
  }
  .contact-divider {
    position: absolute;
    top: 150px;
    left: 318px;
    width: 1px;
    height: 90px;
    background: var(--rule);
  }
  .contact-list {
    position: absolute;
    top: 160px;
    left: 334px;
    list-style: none;
    font-family: "Open Sans", sans-serif;
    font-size: 15px;
    line-height: 20px;
    color: var(--ink-white);
    white-space: nowrap;
  }
  .contact-list li { display: flex; align-items: flex-start; gap: 8px; }
  .contact-icon {
    flex: none;
    width: 14px; height: 14px;
    margin-top: 3px;
    background: var(--ink-white);
    border-radius: 2px;
    display: flex; align-items: center; justify-content: center;
  }
  .contact-list .indent { padding-left: 22px; }

  /* Back */
  .card-back {
    background: linear-gradient(200deg, var(--back-dark-soft) 0%, var(--back-dark) 60%);
    display: flex;
    flex-direction: column;
    align-items: center;
    justify-content: center;
    gap: 8px;
  }
  .back-name {
    font-family: "Bodoni Moda", serif;
    font-weight: 700;
    font-size: 50px;
    color: var(--ink-white);
  }
  .back-services {
    font-family: "Bodoni Moda", serif;
    font-weight: 600;
    font-size: 22px;
    color: var(--ink-white);
    letter-spacing: .5px;
  }
</style>
</head>
<body>

  <section class="card card-front" aria-label="Card front">
    <svg class="front-swoosh" viewBox="0 0 600 343" width="600" height="343" aria-hidden="true">
      <defs>
        <linearGradient id="violetBand" x1="0" y1="0" x2="1" y2="0.5">
          <stop offset="0" stop-color="var(--violet-light)"/>
          <stop offset=".45" stop-color="var(--violet)"/>
          <stop offset="1" stop-color="var(--violet-deep)"/>
        </linearGradient>
      </defs>
      <path d="M0 172 Q300 190 600 343 L0 343 Z" fill="url(#violetBand)"/>
      <path d="M0 186 Q310 202 600 343" fill="none" stroke="var(--card-black)" stroke-width="4"/>
      <path d="M0 163 Q300 180 600 334" fill="none" stroke="var(--card-black)" stroke-width="2"/>
    </svg>

    <h1 class="company-name">Summit BladeLine, Inc.</h1>
    <div class="title-rule"></div>
    <p class="person-name">Harold Tebbets</p>
    <div class="contact-divider"></div>
    <ul class="contact-list">
      <li>
        <span class="contact-icon">
          <svg width="10" height="10" viewBox="0 0 10 10" aria-hidden="true"><path d="M2 1 L4 3 L3 4 Q4 6 6 7 L7 6 L9 8 L8 9 Q3 9 1 2 Z" fill="#000"/></svg>
        </span>
        <span>555-014-2786</span>
      </li>
      <li>
        <span class="contact-icon">
          <svg width="10" height="10" viewBox="0 0 10 10" aria-hidden="true"><rect x="1" y="2.5" width="8" height="5.5" fill="none" stroke="#000" stroke-width="1"/><path d="M1 2.5 L5 6 L9 2.5" fill="none" stroke="#000" stroke-width="1"/></svg>
        </span>
        <span>SummitBladeline@Mailvane.com</span>
      </li>
      <li>
        <span class="contact-icon">
          <svg width="10" height="10" viewBox="0 0 10 10" aria-hidden="true"><path d="M5 9.5 L2 5 A3.2 3.2 0 1 1 8 5 Z" fill="#000"/><circle cx="5" cy="3.8" r="1.1" fill="#fff"/></svg>
        </span>
        <span>2260 W. Orchard Blvd. Unit 4</span>
      </li>
      <li class="indent">Delmar Park, CA 90417</li>
    </ul>
  </section>

  <section class="card card-back" aria-label="Card back">
    <h2 class="back-name">Summit BladeLine</h2>
    <p class="back-services">Airport · Tour guide · Heliport</p>
  </section>

</body>
</html>
```